Book Title: WHEN RIVERS LISTEN

I want to test how good this title is and what is the best cover design for my book

Target Market(s)

Sales people, Entrepreneurs, Public Speakers, Leaders in Business

Font styles to use
Sans Serif

Colors

Designer to choose colors to be used in the design.

Requirements
Must have
• Powerful positive energy emanating from an eagle
Nice to have
• Show an eagle clawing a prey
Should not have
• No negative energies

```html
<!DOCTYPE html>
<html lang="en">
<head>
<meta charset="utf-8">
<title>When Rivers Listen — Book Cover</title>
<link rel="stylesheet" href="https://fonts.googleapis.com/css2?family=Jost:wght@500&display=swap">
<style>
  :root {
    --stage: #ece9e2;
    --cover-black: #0c0b0a;
    --cover-haze: #2b2823;
    --gold-light: #f6d98a;
    --gold-mid: #e2a93c;
    --gold-deep: #b7782a;
    --rule: #c99a45;
  }
  html, body {
    margin: 0;
    padding: 0;
    width: 1200px;
    height: 880px;
    overflow: hidden;
    background: var(--stage);
  }
  .canvas {
    position: relative;
    width: 1200px;
    height: 880px;
    display: flex;
    align-items: center;
    justify-content: center;
  }
  .book-cover {
    position: relative;
    width: 570px;
    height: 800px;
    background:
      radial-gradient(ellipse 55% 80% at 40% 42%, var(--cover-haze) 0%, rgba(43,40,35,0) 70%),
      var(--cover-black);
    overflow: hidden;
  }
  .eagle-art {
    position: absolute;
    left: 250px;
    top: 150px;
    width: 250px;
    height: 170px;
  }
  .title {
    position: absolute;
    left: 60px;
    top: 330px;
    width: 450px;
    margin: 0;
    font-family: "Jost", "Helvetica Neue", Arial, sans-serif;
    font-weight: 500;
    font-size: 72px;
    line-height: 0.98;
    letter-spacing: 0.02em;
    text-transform: uppercase;
  }
  .title-line {
    position: relative;
    display: block;
    width: max-content;
    background: linear-gradient(180deg, var(--gold-light) 0%, var(--gold-mid) 55%, var(--gold-deep) 100%);
    -webkit-background-clip: text;
    background-clip: text;
    color: transparent;
  }
  .title-line--first { margin-left: 90px; }
  .title-line--second { margin-left: 20px; }
  .title-line--third { margin-left: 40px; }
  .title-rule {
    display: block;
    height: 2px;
    background: var(--rule);
    margin: -4px 0 4px;
  }
  .title-rule--upper { width: 300px; margin-left: 30px; }
  .title-rule--lower { width: 330px; margin-left: 50px; }
</style>
</head>
<body>
  <main class="canvas">
    <section class="book-cover">
      <svg class="eagle-art" role="img" aria-label="Golden eagle with spread wings, talons reaching down" viewBox="0 0 250 170">
        <defs>
          <radialGradient id="eagleGlow" cx="50%" cy="45%" r="55%">
            <stop offset="0%" stop-color="#f6d98a"/>
            <stop offset="60%" stop-color="#e2a93c" stop-opacity="0.85"/>
            <stop offset="100%" stop-color="#b7782a" stop-opacity="0"/>
          </radialGradient>
        </defs>
        <ellipse cx="125" cy="85" rx="125" ry="85" fill="url(#eagleGlow)"/>
      </svg>
      <h1 class="title">
        <span class="title-line title-line--first">When</span>
        <span class="title-rule title-rule--upper"></span>
        <span class="title-line title-line--second">Rivers</span>
        <span class="title-rule title-rule--lower"></span>
        <span class="title-line title-line--third">Listen</span>
      </h1>
    </section>
  </main>
</body>
</html>
```